CARPET CLEANING FLYER WINDOW WASHING FLYER

Double Sided Flyer with QRVP Stamp in top corner
FLYER IS ALMOST COMPLETE......
Looking to enhance the layout and optimize the font

Would like to incorporate the van into the layout and make it look like it really fits in. I'd like to eliminate the white box I only need the QRVP stamp label

Use the silver metallic font everywhere that it looks good

Target Market(s)

residential home owners

Contact Information for Business Card

Design is almost complete, I will upload most recent version and label it

Font styles to use
Sans Serif

Colors
3277b5
ec1f27
00a990
9bcb3c
fece3e
a5d8ed
33a6d7

Requirements
Must have
• Remove the big white mailing label and only use QRVP Stamp
• On bottom of both sides remove/replace all contact info with logo uploaded today
• Keep logo/contact info to the bottom right (I want free space on left half of bottom)
• Replace FONT with SILVER FONT uploaded.... Change Color of Silver Font as Needed
• Integrate picture of van onto flyer
• On top of both sides reduce size of FREE ESTIMATES to 3/4 Current and justify left....

```html
<!DOCTYPE html>
<html lang="en">
<head>
<meta charset="utf-8">
<title>Eco Friendly Cleaning Flyer</title>
<link href="https://fonts.googleapis.com/css2?family=Montserrat:wght@500;700;800;900&family=Open+Sans:wght@400;600&display=swap" rel="stylesheet">
<style>
  :root{
    --navy:#13224a;
    --navy-deep:#0c1733;
    --blue:#3277b5;
    --sky:#33a6d7;
    --light-sky:#a5d8ed;
    --yellow:#fece3e;
    --green:#9bcb3c;
    --teal:#00a990;
    --red:#ec1f27;
    --white:#ffffff;
    --ink:#24324f;
    --grey:#6b7488;
  }
  *{box-sizing:border-box;margin:0;padding:0}
  html,body{width:793px;height:1200px;overflow:hidden;background:#fff}
  .flyer{position:relative;width:793px;height:1200px;background:var(--white);font-family:"Open Sans",sans-serif;color:var(--ink);overflow:hidden}

  .top-band{position:absolute;left:0;top:0;width:793px;height:80px;background:var(--white)}
  .brand{position:absolute;left:36px;top:20px;display:flex;align-items:center;gap:10px}
  .brand-dot{width:38px;height:38px;border-radius:50%;background:var(--sky)}
  .brand-name{font-family:"Montserrat",sans-serif;font-weight:800;font-size:19px;color:var(--blue);line-height:1}
  .brand-tag{font-family:"Montserrat",sans-serif;font-weight:800;font-size:11px;color:var(--blue);letter-spacing:2px;margin-top:4px}

  .hero{position:absolute;left:0;top:80px;width:793px;height:470px;background:linear-gradient(160deg,var(--navy) 0%,var(--navy-deep) 100%)}
  .hero-photo{position:absolute;right:0;top:80px;width:390px;height:520px;background:linear-gradient(180deg,#2a3a66 0%,#c9b3a3 45%,#e9dfd6 100%)}
  .headline{position:absolute;left:40px;top:118px;width:350px}
  .headline .eco{font-family:"Montserrat",sans-serif;font-weight:500;font-size:32px;color:var(--white);letter-spacing:1px;line-height:1.1}
  .headline .cleaning{font-family:"Montserrat",sans-serif;font-weight:900;font-size:54px;color:var(--yellow);line-height:1.05}
  .hero-copy{position:absolute;left:40px;top:222px;width:330px;font-size:13px;line-height:1.5;color:#d7dcea}

  .services{position:absolute;left:36px;top:300px;width:330px;height:710px;background:var(--white);border-radius:12px;box-shadow:0 6px 18px rgba(12,23,51,.25);overflow:hidden}
  .services-head{background:var(--blue);padding:16px 24px;font-family:"Montserrat",sans-serif;font-weight:800;font-size:24px;color:var(--white)}
  .services-head span{color:var(--yellow)}
  .service-list{list-style:none;padding:14px 22px}
  .service{display:flex;align-items:center;gap:16px;padding:20px 0;border-bottom:1px solid #e3e8f0}
  .service:last-child{border-bottom:none}
  .service-icon{flex:none;width:50px;height:50px;border-radius:50%;background:var(--sky);display:flex;align-items:center;justify-content:center}
  .service-title{font-family:"Montserrat",sans-serif;font-weight:800;font-size:16px;color:var(--navy)}
  .service-title b{color:var(--blue)}
  .service-desc{font-size:12px;color:var(--grey);margin-top:3px}

  .call-box{position:absolute;left:403px;top:600px;width:390px;height:150px;background:var(--blue);padding:28px 0 0 34px}
  .call-label{font-family:"Montserrat",sans-serif;font-weight:800;font-size:26px;color:var(--white)}
  .call-phone{display:flex;align-items:center;gap:10px;margin-top:8px;font-family:"Montserrat",sans-serif;font-weight:900;font-size:38px;color:var(--yellow);white-space:nowrap}

  .best{position:absolute;left:403px;top:790px;width:355px}
  .best-title{font-family:"Montserrat",sans-serif;font-weight:800;font-size:21px;color:var(--navy)}
  .best-title span{color:var(--blue)}
  .best-rule{width:70px;height:4px;background:var(--yellow);margin:10px 0 14px}
  .best-copy{font-size:14px;line-height:1.6;color:var(--grey)}

  .footer{position:absolute;left:0;top:1040px;width:793px;height:160px;border-top:4px solid var(--blue)}
  .footer .brand{left:36px;top:36px}
  .contacts{position:absolute;left:403px;top:30px;width:355px;display:flex;flex-direction:column;gap:12px}
  .contact{display:flex;gap:10px;align-items:center;font-size:13px;line-height:1.4;color:var(--ink);white-space:nowrap}
  .contact svg{flex:none}
  .footer-bar{position:absolute;left:0;bottom:0;width:793px;height:34px;background:var(--navy)}
</style>
</head>
<body>
<div class="flyer">
  <div class="top-band"></div>
  <div class="brand">
    <div class="brand-dot"></div>
    <div><div class="brand-name">BrightNest Cleaning</div><div class="brand-tag">CLEANING SERVICES</div></div>
  </div>

  <section class="hero"></section>
  <div class="hero-photo" role="img" aria-label="Smiling cleaner in apron and gloves holding a basket of cleaning supplies"></div>

  <h1 class="headline">
    <div class="eco">ECO FRIENDLY</div>
    <div class="cleaning">CLEANING</div>
  </h1>
  <p class="hero-copy">Safe, green cleaning for every room of your home, done by trained local pros who care about details.</p>

  <section class="services">
    <h2 class="services-head">OUR <span>SERVICES</span></h2>
    <ul class="service-list">
      <li class="service"><div class="service-icon"><svg width="22" height="22" viewBox="0 0 24 24"><path d="M4 12l5 5 11-11" fill="none" stroke="#fff" stroke-width="3"/></svg></div><div><div class="service-title">CARPET <b>CLEANING</b></div><div class="service-desc">Deep steam clean, fast drying</div></div></li>
      <li class="service"><div class="service-icon"><svg width="22" height="22" viewBox="0 0 24 24"><path d="M4 12l5 5 11-11" fill="none" stroke="#fff" stroke-width="3"/></svg></div><div><div class="service-title">WINDOW <b>WASHING</b></div><div class="service-desc">Streak free glass inside out</div></div></li>
      <li class="service"><div class="service-icon"><svg width="22" height="22" viewBox="0 0 24 24"><path d="M4 12l5 5 11-11" fill="none" stroke="#fff" stroke-width="3"/></svg></div><div><div class="service-title">WATER <b>DAMAGE</b></div><div class="service-desc">Quick help after leaks, floods</div></div></li>
      <li class="service"><div class="service-icon"><svg width="22" height="22" viewBox="0 0 24 24"><path d="M4 12l5 5 11-11" fill="none" stroke="#fff" stroke-width="3"/></svg></div><div><div class="service-title">TILE &amp; <b>GROUT</b></div><div class="service-desc">Restore shine to every joint</div></div></li>
      <li class="service"><div class="service-icon"><svg width="22" height="22" viewBox="0 0 24 24"><path d="M4 12l5 5 11-11" fill="none" stroke="#fff" stroke-width="3"/></svg></div><div><div class="service-title"><b>MAINTENANCE</b></div><div class="service-desc">Regular visits keep homes fresh</div></div></li>
      <li class="service"><div class="service-icon"><svg width="22" height="22" viewBox="0 0 24 24"><path d="M4 12l5 5 11-11" fill="none" stroke="#fff" stroke-width="3"/></svg></div><div><div class="service-title">POWER <b>WASHING</b></div><div class="service-desc">Driveways, decks and siding cleaned</div></div></li>
    </ul>
  </section>

  <section class="call-box">
    <div class="call-label">CALL US TODAY !!!</div>
    <div class="call-phone">
      <svg width="30" height="30" viewBox="0 0 24 24"><path d="M6.6 10.8a15 15 0 006.6 6.6l2.2-2.2a1 1 0 011-.25 11.4 11.4 0 003.6.57 1 1 0 011 1V20a1 1 0 01-1 1A17 17 0 013 4a1 1 0 011-1h3.5a1 1 0 011 1c0 1.25.2 2.45.57 3.57a1 1 0 01-.25 1z" fill="#fece3e"/></svg>
      555-014-2290
    </div>
  </section>

  <section class="best">
    <h2 class="best-title">WE PROVIDE <span>BEST SERVICES</span></h2>
    <div class="best-rule"></div>
    <p class="best-copy">Our friendly team uses plant based products that are safe for kids, pets and the planet. We arrive on time, work carefully and leave every space spotless. Book today and enjoy a cleaner, healthier home.</p>
  </section>

  <footer class="footer">
    <div class="brand">
      <div class="brand-dot"></div>
      <div><div class="brand-name">BrightNest Cleaning</div><div class="brand-tag">CLEANING SERVICES</div></div>
    </div>
    <div class="contacts">
      <div class="contact">
        <svg width="16" height="20" viewBox="0 0 24 30"><path d="M12 0a10 10 0 00-10 10c0 8 10 20 10 20s10-12 10-20A10 10 0 0012 0zm0 14a4 4 0 110-8 4 4 0 010 8z" fill="#3277b5"/></svg>
        <span>214 Harbor Lane, Suite 3, Bayview</span>
      </div>
      <div class="contact">
        <svg width="18" height="14" viewBox="0 0 24 18"><rect x="1" y="1" width="22" height="16" rx="2" fill="none" stroke="#3277b5" stroke-width="2"/><path d="M2 2l10 8 10-8" fill="none" stroke="#3277b5" stroke-width="2"/></svg>
        <span>hello@brightnestclean.com</span>
      </div>
    </div>
    <div class="footer-bar"></div>
  </footer>
</div>
</body>
</html>
```